A Label for an ECO Friendly Spirit Company

Design a label which can be used for vodka and gin (London Dry Gin). It should be Square type Like the Shape File you see in the uploads. VORK means Local Eco friendly Authentic and Fair. We want a cool and slim label that calls for eco-friendly. We want to use it for our premium
Vodka and our London Dry Gin. Please use the logo and design it in Square Type.

40%vol, 700ml

Target Market(s)

spirits and events

Industry/Entity Type

SPIRITS

Colors
00AB8E
00BBA5
67D7C9
C6EFE9
E9F9F6
59FF00
82FF00
B8FF75
E3FFCB
F4FFEA

Requirements
Must have
• Logo from VORK, Squaee Shape

```html
<!DOCTYPE html>
<html lang="en">
<head>
<meta charset="utf-8">
<title>VORK Vodka Label</title>
<link rel="stylesheet" href="https://fonts.googleapis.com/css2?family=Montserrat:wght@600;700&display=swap">
<style>
  :root {
    --backdrop: #eef0f2;
    --label-white: #ffffff;
    --teal: #24b092;
    --lime: #8dc63f;
  }
  html, body {
    margin: 0;
    padding: 0;
    width: 1085px;
    height: 1200px;
    overflow: hidden;
    background: var(--backdrop);
  }
  .label {
    display: block;
    width: 1085px;
    height: 1200px;
  }
  .label-base { fill: var(--label-white); }
  .frame-line {
    fill: none;
    stroke: var(--teal);
    stroke-width: 6;
    stroke-linejoin: miter;
  }
  .brand-square { fill: var(--lime); }
  .brand-name {
    font-family: "Montserrat", sans-serif;
    font-weight: 700;
    font-size: 96px;
    fill: var(--teal);
    letter-spacing: 2px;
  }
  .spirit-type,
  .edge-info {
    font-family: "Montserrat", sans-serif;
    font-weight: 700;
    fill: var(--lime);
  }
  .spirit-type { font-size: 30px; letter-spacing: 1px; }
  .edge-info { font-size: 27px; }
  .pointer { fill: var(--teal); }
</style>
</head>
<body>
<svg class="label" viewBox="0 0 1085 1200" xmlns="http://www.w3.org/2000/svg" aria-label="VORK vodka label">
  <g transform="translate(542 600) scale(1.4) translate(-910 -1155)">
    <polygon class="label-base" points="910,798 1267,1155 910,1512 553,1155"/>

    <path class="frame-line" d="M685 1235 L605 1155 L910 850 L1215 1155 L1135 1235"/>
    <path class="frame-line" d="M797 1347 L910 1460 L1023 1347"/>

    <rect class="brand-square" x="860" y="1030" width="100" height="100" rx="8"/>
    <text class="brand-name" x="910" y="1236" text-anchor="middle">VORK</text>

    <text class="spirit-type" x="910" y="1322" text-anchor="middle">VODKA</text>
    <polygon class="pointer" points="825,1336 995,1336 910,1421"/>

    <text class="edge-info" text-anchor="middle" transform="translate(740 1283) rotate(45)">40%VOL</text>
    <text class="edge-info" text-anchor="middle" transform="translate(1080 1283) rotate(-45)">700ml</text>
  </g>
</svg>
</body>
</html>
```